Reed & Vale NC grand opening (for BILLBOARD)

Advertising the grand opening of our cannabis/hemp shop in NC. We will sell all things hemp (flower, cartridges, disposables, edibles, creams, lotions, pet products etc...)

Requirements
Must have
• include, open starting Aug 1, but grand opening Aug 15th.
Nice to have
• Difference slogan ideas "Save some cash, buy our grass" "Find your perfect high at Reed & Vale cannabis store" "Experience Nature's Gift: Reed & Vale Cannabis Store"

```html
<!DOCTYPE html>
<html lang="en">
<head>
<meta charset="UTF-8">
<title>Reed &amp; Vale Grand Opening Billboard</title>
<link rel="stylesheet" href="https://fonts.googleapis.com/css2?family=Montserrat:wght@500;600&family=Roboto+Condensed:wght@700&display=swap">
<style>
  :root {
    --page-grey: #cbcbcb;
    --white: #ffffff;
    --navy: #0f1238;
    --brand-navy: #1c1d45;
    --teal: #3fa4b3;
    --green-light: #9be47c;
    --green-mid: #64a24a;
    --sky-teal: #38a7c6;
    --leaf-dark: #03683c;
  }
  * { margin: 0; padding: 0; box-sizing: border-box; }
  html, body {
    width: 1200px; height: 576px; overflow: hidden;
    background: var(--page-grey);
  }
  .billboard {
    position: absolute; left: 50px; top: 127px;
    width: 1100px; height: 321px;
    background: var(--white);
    overflow: hidden;
  }
  .hero-panel {
    position: absolute; left: 323px; top: 0; width: 777px; height: 100%;
    background:
      radial-gradient(ellipse 60% 90% at 100% 30%, rgba(56,167,198,0.85), rgba(56,167,198,0) 70%),
      linear-gradient(to bottom, var(--green-light) 0%, var(--green-mid) 55%, var(--sky-teal) 100%);
  }
  .tagline-band {
    position: absolute; left: 0; top: 0; width: 400px; height: 100%;
  }
  .leaf-illustration {
    position: absolute; left: 222px; top: 0; width: 330px; height: 321px;
    background: radial-gradient(ellipse 42% 46% at 58% 52%, var(--leaf-dark) 0%, var(--leaf-dark) 60%, rgba(3,104,60,0) 100%);
  }
  .brand-name {
    position: absolute; left: 12px; top: 72px; width: 290px;
    text-align: center;
    font-family: 'Montserrat', sans-serif; font-weight: 600;
    font-size: 42px; line-height: 52px; color: var(--brand-navy);
    letter-spacing: -0.5px;
    z-index: 2;
  }
  .tagline {
    position: absolute; left: 10px; top: 178px; width: 222px;
    text-align: center;
    font-family: 'Montserrat', sans-serif; font-weight: 500;
    font-size: 24px; line-height: 27.5px; color: var(--white);
    z-index: 2;
  }
  .headline {
    position: absolute; left: 566px; top: 16px;
    font-family: 'Roboto Condensed', sans-serif; font-weight: 700;
    font-size: 74px; line-height: 58px; text-transform: uppercase;
    z-index: 2;
  }
  .headline .line { display: block; white-space: nowrap; }
  .headline .light { color: var(--white); }
  .headline .dark { color: var(--navy); }
  .headline sup { font-size: 32px; vertical-align: baseline; }
</style>
</head>
<body>
  <main class="billboard">
    <div class="hero-panel"></div>
    <svg class="tagline-band" viewBox="0 0 400 321" aria-hidden="true">
      <polygon points="0,186 115,154 260,186 260,321 0,321" fill="var(--teal)"/>
    </svg>
    <div class="leaf-illustration" role="img" aria-label="Large green cannabis leaf illustration with a yellow outline"></div>
    <div class="brand-name">Reed &amp; Vale</div>
    <p class="tagline">Find your<br>Perfect High<br>at<br>REED &amp; VALE<br>Cannabis Store</p>
    <h1 class="headline">
      <span class="line light">Open Starting</span>
      <span class="line dark">Aug 1</span>
      <span class="line light">But</span>
      <span class="line light">Grand Opening</span>
      <span class="line dark">Aug 15<sup>th</sup></span>
    </h1>
  </main>
</body>
</html>
```